Design a Ketone Test Strip Label and Box for Formed From Vale

Design a product label and a box design for a Ketone Test Strip product for the company Formed From Vale.
*Please use the template of the box and label .ai file will be provided.*
Please see example of other competitors for inspiration
Use the text/look instructions from the provided product examples
*MUST HAVE BARCODE ON BOX*

Industry/Entity Type

It Company

Font styles to use
Sans Serif

Colors

Designer to choose colors to be used in the design.

Requirements
Must have
• *MUST HAVE BARCODE ON BOX*
• Must use the .ai templates provided.
• LEFT OF LABEL Layout/text:
• FormedFromVale.com
• Formed From Vale Logo
• MFG:
• EXP:
• IMPORTANT
• Keep away from light and moisture.
• Promptly replace cap after taking out strips.
• Do not remove desiccants.
• Do not touch test areas of reagent strips.
• Use within the expiration date.
• Read insert carefully before use.
• 100 Ketone Test Strips
• MIDDLE/RIGHT SIDE OF LABEL layout/text:
• KETONE TEST STRIPS
• (to the left) TESTING COLOR CHART (going down vertically)
• (to the right) Love Keto? Visit: FormedFromVale.com
• How to test
• 1.Firmly hold end farthest away from test pad. Pass test pad through
• urine stream or place inside a urine filled cup
• 2. After 40 seconds, match the test pad
• to the color chart shown on the bottle.
• Any other symbols in the template placed at the bottom.
• FRONT OF BOX:
• Formed From Vale Logo
• Ketone Test Strips
• Reagent Strips for Urinalysis
• Color Chart Going Horizontal
• Instant Results
• Most Accurate
• Easy to Use
• Pharmaceutical Grade
• 100 Strips
• LEFT OF BOX:
• RIGHT OF BOX:
• BACK OF BOX:
Nice to have
• Clean simple design
Should not have
• be too busy

```html
<!DOCTYPE html>
<html lang="en">
<head>
<meta charset="utf-8">
<title>Formed From Vale – Ketone Test Strips Box</title>
<link rel="stylesheet" href="https://fonts.googleapis.com/css2?family=Montserrat:wght@400;500;600;700;800&display=swap">
<style>
  :root {
    --page: #ffffff;
    --teal: #58c4c6;
    --white: #ffffff;
    --navy: #2c3d4f;
    --chart-1: #fbd7b9;
    --chart-2: #f8c3b0;
    --chart-3: #f3a3ae;
    --chart-4: #e67a93;
    --chart-5: #c9628a;
    --chart-6: #a5577e;
    --art: #e9f6f6;
  }
  html, body { margin: 0; padding: 0; overflow: hidden; background: var(--page); }
  .canvas { width: 1200px; height: 2296px; position: relative; overflow: hidden; background: var(--page); }
  .dieline { position: absolute; left: 0; top: 0; width: 1200px; height: 2296px; }
  .box-fill { fill: var(--teal); }
  .c1 { fill: var(--chart-1); } .c2 { fill: var(--chart-2); } .c3 { fill: var(--chart-3); }
  .c4 { fill: var(--chart-4); } .c5 { fill: var(--chart-5); } .c6 { fill: var(--chart-6); }
  text { font-family: 'Montserrat', sans-serif; }
  .brand { fill: var(--navy); font-weight: 700; font-size: 10.5px; letter-spacing: .3px; text-anchor: middle; }
  .brand-square { fill: var(--navy); }
  .product-title { fill: var(--white); font-weight: 800; font-size: 25px; text-anchor: middle; letter-spacing: .5px; }
  .pill { fill: var(--white); }
  .pill-text { fill: var(--teal); font-weight: 800; font-size: 8.5px; text-anchor: middle; letter-spacing: .4px; }
  .pill-text-lg { fill: var(--teal); font-weight: 800; font-size: 9.5px; text-anchor: middle; letter-spacing: .3px; }
  .scale-label { fill: var(--white); font-weight: 600; font-size: 4.5px; letter-spacing: .2px; }
  .claims { fill: var(--white); font-weight: 600; font-size: 9.5px; text-anchor: middle; letter-spacing: 1px; }
  .heading { fill: var(--white); font-weight: 800; font-size: 7.5px; letter-spacing: .2px; }
  .body { fill: var(--white); font-weight: 500; font-size: 7.3px; }
  .body-num { fill: var(--white); font-weight: 800; font-size: 8px; }
  .site { fill: var(--white); font-weight: 500; font-size: 8.5px; text-anchor: middle; }
  .meta { fill: var(--white); font-weight: 500; font-size: 8.5px; }
  .love { fill: var(--white); font-weight: 500; font-size: 8.5px; text-anchor: middle; }
  .icon-line { fill: none; stroke: var(--white); stroke-width: 1.1; }
  .icon-text { fill: var(--white); font-weight: 600; font-size: 9px; text-anchor: middle; }
  .chart-label { fill: var(--white); font-weight: 700; font-size: 3.6px; text-anchor: middle; }
  .chart-side { fill: var(--white); font-weight: 600; font-size: 3px; }
  .badge { fill: var(--white); }
  .art-area { fill: var(--art); }
</style>
</head>
<body>
<div class="canvas">
<svg class="dieline" viewBox="0 257 784 1500" xmlns="http://www.w3.org/2000/svg">
  <defs>
    <g id="chart-row">
      <rect class="c1" x="0" y="0" width="17" height="13"/>
      <rect class="c2" x="20" y="0" width="17" height="13"/>
      <rect class="c3" x="40" y="0" width="17" height="13"/>
      <rect class="c4" x="60" y="0" width="17" height="13"/>
      <rect class="c5" x="80" y="0" width="17" height="13"/>
      <rect class="c6" x="100" y="0" width="17" height="13"/>
    </g>
    <g id="chart-row-thin">
      <rect class="c1" x="0" y="0" width="17" height="6"/>
      <rect class="c2" x="20" y="0" width="17" height="6"/>
      <rect class="c3" x="40" y="0" width="17" height="6"/>
      <rect class="c4" x="60" y="0" width="17" height="6"/>
      <rect class="c5" x="80" y="0" width="17" height="6"/>
      <rect class="c6" x="100" y="0" width="17" height="6"/>
    </g>
    <g id="brand-mark">
      <rect class="brand-square" x="-58" y="-8" width="8" height="8"/>
      <text class="brand" x="4" y="0">Formed From Vale</text>
    </g>
    <g id="count-pill">
      <rect class="pill" x="-63" y="-7.5" width="126" height="15" rx="7.5"/>
      <text class="pill-text-lg" x="0" y="3.4">100 TEST STRIPS</text>
    </g>
  </defs>

  <!-- box outline -->
  <g class="box-outline">
    <path class="box-fill" d="M55 848 L68 835 L240 835 L240 1198 L68 1198 L55 1186 Z"/>
    <path class="box-fill" d="M95 1198 L240 1198 L240 1372 Q240 1385 227 1385 L108 1385 Q95 1385 95 1372 Z"/>
    <rect class="box-fill" x="240" y="835" width="480" height="363"/>
    <path class="box-fill" d="M240 835 L240 812 L266 728 Q267 725 272 725 L405 725 L405 835 Z"/>
    <path class="box-fill" d="M565 835 L565 725 L696 725 Q700 725 701 728 L720 812 L720 835 Z"/>
    <rect class="box-fill" x="405" y="668" width="160" height="170"/>
    <path class="box-fill" d="M409 668 L409 648 Q409 630 427 630 L543 630 Q561 630 561 648 L561 668 Z"/>
    <path class="box-fill" d="M240 1198 L405 1198 L405 1242 L392 1255 L256 1255 L240 1232 Z"/>
    <path class="box-fill" d="M405 1198 L565 1198 L565 1232 L549 1255 L421 1255 L405 1242 Z"/>
    <path class="box-fill" d="M565 1198 L720 1198 L720 1320 L580 1320 L580 1220 Z"/>
  </g>

  <!-- top flap -->
  <g class="top-flap">
    <rect class="c1" x="428" y="676" width="15" height="66"/>
    <rect class="c2" x="448" y="676" width="15" height="66"/>
    <rect class="c3" x="468" y="676" width="15" height="66"/>
    <rect class="c4" x="488" y="676" width="15" height="66"/>
    <rect class="c5" x="508" y="676" width="15" height="66"/>
    <rect class="c6" x="527" y="676" width="15" height="66"/>
    <g transform="rotate(180 485 775)">
      <rect class="pill" x="450" y="744" width="70" height="11" rx="5.5"/>
      <text class="pill-text" x="485" y="752.5" style="font-size:7px">TEST STRIPS</text>
      <text class="product-title" x="485" y="773" style="font-size:20px">KETONE</text>
      <use href="#brand-mark" transform="translate(485 795)"/>
    </g>
  </g>

  <!-- front panel -->
  <g class="panel-front">
    <use href="#chart-row" x="112" y="835"/>
    <use href="#brand-mark" transform="translate(151 884)"/>
    <use href="#chart-row-thin" x="112" y="910"/>
    <text class="product-title" x="168" y="951">KETONE</text>
    <rect class="pill" x="132" y="957" width="76" height="13" rx="6.5"/>
    <text class="pill-text" x="170" y="966">TEST STRIPS</text>
    <use href="#chart-row" x="112" y="993" transform="translate(0 0)"/>
    <text class="scale-label" x="112" y="1019">LESS ◄——— KEYTONES ———► MORE</text>
    <text class="claims" x="170" y="1117">INSTANT RESULTS</text>
    <text class="claims" x="170" y="1129">MOST ACCURATE</text>
    <text class="claims" x="170" y="1141">EASY TO USE</text>
    <use href="#chart-row" x="112" y="1157"/>
    <use href="#count-pill" transform="translate(170 1190)"/>
  </g>

  <!-- symbols and chart panel -->
  <g class="panel-symbols">
    <use href="#chart-row" x="266" y="835"/>
    <use href="#brand-mark" transform="translate(326 874)"/>
    <use href="#chart-row-thin" x="266" y="910"/>
    <circle class="icon-line" cx="288" cy="1003" r="8"/>
    <line class="icon-line" x1="282" y1="1009" x2="294" y2="997"/>
    <text class="icon-text" x="288" y="1006">2</text>
    <rect class="icon-line" x="274" y="1040" width="28" height="15"/>
    <text class="icon-text" x="288" y="1051">IVD</text>
    <rect class="icon-line" x="276" y="1083" width="22" height="17"/>
    <line class="icon-line" x1="287" y1="1083" x2="287" y2="1100"/>
    <text class="icon-text" x="293" y="1096" style="font-size:7px">i</text>
    <line class="icon-line" x1="283" y1="1125" x2="283" y2="1150"/>
    <path class="icon-line" d="M283 1125 H293 M283 1150 H273"/>
    <text class="chart-side" x="292" y="1130" style="font-size:5px">+30°C</text>
    <text class="chart-side" x="262" y="1153" style="font-size:5px">+2°C</text>
    <text class="chart-label" x="361" y="998">MATCH THE</text>
    <text class="chart-label" x="361" y="1003">TEST PAD</text>
    <line class="icon-line" x1="341" y1="1010" x2="341" y2="1166" style="stroke-width:.5"/>
    <rect class="c1" x="350" y="1010" width="22" height="22"/>
    <rect class="c2" x="350" y="1036" width="22" height="22"/>
    <rect class="c3" x="350" y="1062" width="22" height="22"/>
    <rect class="c4" x="350" y="1088" width="22" height="22"/>
    <rect class="c5" x="350" y="1114" width="22" height="22"/>
    <rect class="c6" x="350" y="1140" width="22" height="22"/>
    <text class="chart-side" x="336" y="1014">LESS</text>
    <text class="chart-side" x="336" y="1165">MORE</text>
    <use href="#count-pill" transform="translate(327 1190)"/>
  </g>

  <!-- how to test panel -->
  <g class="panel-instructions">
    <use href="#chart-row" x="427" y="822"/>
    <use href="#brand-mark" transform="translate(488 874)"/>
    <use href="#chart-row-thin" x="427" y="910"/>
    <text class="heading" x="425" y="944">HOW TO TEST</text>
    <text class="body-num" x="425" y="955">1.</text>
    <text class="body"><tspan x="433" y="955">Firmly hold end</tspan><tspan x="433" y="964">farthest away</tspan><tspan x="433" y="973">from test pad.</tspan><tspan x="433" y="982">Pass test pad</tspan><tspan x="433" y="991">through- urine</tspan><tspan x="433" y="1000">stream or place</tspan><tspan x="433" y="1009">inside a urine</tspan><tspan x="433" y="1018">filled cup</tspan></text>
    <rect class="art-area" x="492" y="935" width="58" height="80" rx="4" role="img" aria-label="Illustration of a hand dipping a test strip into a urine cup"/>
    <rect class="c1" x="438" y="1035" width="8" height="7"/>
    <rect class="c2" x="438" y="1044" width="8" height="7"/>
    <rect class="c3" x="438" y="1053" width="8" height="7"/>
    <rect class="c4" x="438" y="1062" width="8" height="7"/>
    <rect class="c5" x="438" y="1071" width="8" height="7"/>
    <rect class="c6" x="438" y="1080" width="8" height="7"/>
    <rect class="art-area" x="452" y="1040" width="96" height="30" rx="4" role="img" aria-label="Illustration of a hand holding a test strip beside the colour chart"/>
    <text class="body-num" x="462" y="1084">2.</text>
    <text class="body"><tspan x="472" y="1084">After 40</tspan><tspan x="472" y="1093">seconds, match the</tspan><tspan x="472" y="1102">test pad to the color</tspan><tspan x="472" y="1111">chart shown on the</tspan><tspan x="472" y="1120">bottle.</tspan></text>
    <rect class="badge" x="455" y="1133" width="20" height="12" rx="2"/>
    <rect class="badge" x="483" y="1133" width="26" height="12" rx="2"/>
    <text class="love" x="485" y="1164">Love Keto?</text>
    <text class="love" x="485" y="1177">Visit: FormedFromVale.com</text>
  </g>

  <!-- important panel -->
  <g class="panel-important">
    <use href="#chart-row" x="584" y="835"/>
    <use href="#brand-mark" transform="translate(645 874)"/>
    <use href="#chart-row-thin" x="584" y="910"/>
    <rect class="pill" x="602" y="958" width="80" height="13" rx="6.5"/>
    <text class="pill-text" x="642" y="967.5" style="font-size:9px">IMPORTANT</text>
    <text class="body"><tspan x="598" y="988">•Keep away from light</tspan><tspan x="600" y="997">and moisture.</tspan><tspan x="598" y="1012">•Promptly replace cap</tspan><tspan x="600" y="1021">after taking out strips.</tspan><tspan x="598" y="1036">•Do not remove</tspan><tspan x="600" y="1045">desiccants.</tspan><tspan x="598" y="1060">•Do not touch test areas</tspan><tspan x="600" y="1069">of reagent strips.</tspan><tspan x="598" y="1084">•Use within the</tspan><tspan x="600" y="1093">expiration date.</tspan><tspan x="598" y="1108">•Read insert carefully</tspan><tspan x="600" y="1117">before use.</tspan></text>
    <text class="site" x="642" y="1129">FormedFromVale.com</text>
    <text class="meta" x="610" y="1158">MFG:</text>
    <text class="meta" x="610" y="1170">EXP:</text>
    <use href="#count-pill" transform="translate(642 1190)"/>
  </g>
</svg>
</div>
</body>
</html>
```